Belford & Company

We are a boutique commercial real estate firm. For our Business card design - sleek, modern, yet high-end/classy. Please see our website: belfordandcompany.example for details.

We currently need 2 business card names and the ability to add/change the business card information -
Name, Title, Address, Office #, Mobile #, Fax, Email and company website.

Industry/Entity Type

Real Estate

Contact Information for Business Card

Business card design - sleek, modern, yet high-end/classy. Please see our website: belfordandcompany.example for details.

Also, we'd like to have our slogan "Precision Shapes Every Outcome." somewhere in there. We'd like to make some part of it raised or a different texture if possible.
Color #'s:
blue 19 36 128
light gray 222 222 221
dark gray 107 120 128

Also, we'd like to have our slogan "Precision Shapes Every Outcome." somewhere in there. We'd like to make some part of it raised or a different texture if possible - grey on one side and blue on the other - rounded edges preferred. Maybe either metal/silver/grey raised logo on the back. Thank you!!

Requirements
Must have
• Sleek, modern, clean and classy design

```html
<!DOCTYPE html>
<html lang="en">
<head>
<meta charset="utf-8">
<title>Belford &amp; Company — Business Card</title>
<link rel="stylesheet" href="https://fonts.googleapis.com/css2?family=Open+Sans:wght@400;600;700&display=swap">
<style>
  :root {
    --brand-blue: #1a3a93;
    --brand-blue-deep: #132480;
    --light-gray: #dededd;
    --dark-gray: #6b7880;
    --silver-1: #f4f4f3;
    --silver-2: #c9c9c8;
    --stage: #d4d6d8;
    --text-light: #f2f3f4;
    --text-muted: #d9dcde;
  }
  * { box-sizing: border-box; margin: 0; padding: 0; }
  html, body { width: 1200px; height: 1021px; overflow: hidden; }
  body {
    background: var(--stage);
    font-family: "Open Sans", Arial, sans-serif;
    display: flex;
    flex-direction: column;
    align-items: center;
    justify-content: center;
    gap: 47px;
  }
  .card {
    width: 770px;
    height: 440px;
    border-radius: 30px;
    position: relative;
    box-shadow: 0 6px 18px rgba(0,0,0,0.18);
  }

  /* Front: blue with silver panel */
  .card--front {
    background: linear-gradient(160deg, #1f44a6, var(--brand-blue-deep));
    display: flex;
    align-items: center;
    justify-content: center;
  }
  .silver-panel {
    width: 420px;
    height: 210px;
    background: linear-gradient(135deg, var(--silver-1), var(--silver-2));
    padding: 8px;
  }
  .silver-panel__frame {
    width: 100%;
    height: 100%;
    border: 2px solid var(--brand-blue);
    display: flex;
    align-items: center;
    justify-content: center;
    gap: 14px;
  }
  .wordmark {
    font-weight: 700;
    font-size: 34px;
    letter-spacing: 1px;
    text-transform: uppercase;
    line-height: 1.05;
    text-align: left;
  }
  .silver-panel .wordmark { color: var(--brand-blue); }
  .wordmark-square { width: 26px; height: 26px; flex: none; }
  .silver-panel .wordmark-square { background: var(--brand-blue); }

  /* Back: grey with blue logo panel and contact details */
  .card--back {
    background: var(--dark-gray);
    color: var(--text-light);
  }
  .blue-panel {
    position: absolute;
    left: 250px; top: 36px;
    width: 300px; height: 150px;
    background: var(--brand-blue);
    border: 3px solid #8a96a6;
    display: flex;
    align-items: center;
    justify-content: center;
    gap: 12px;
  }
  .blue-panel .wordmark { color: var(--light-gray); font-size: 25px; }
  .blue-panel .wordmark-square { background: var(--light-gray); width: 20px; height: 20px; }

  .details {
    position: absolute;
    left: 40px; right: 30px; top: 206px;
    display: flex;
  }
  .identity {
    width: 340px;
    text-align: right;
    padding-right: 26px;
    border-right: 1.5px solid var(--text-muted);
    white-space: nowrap;
  }
  .identity__name { font-weight: 700; font-size: 24px; line-height: 1.1; }
  .identity__title { font-size: 19px; color: var(--text-muted); margin-bottom: 10px; }
  .identity__address { font-size: 18px; line-height: 1.3; color: var(--text-muted); }

  .contacts {
    list-style: none;
    padding-left: 24px;
    padding-top: 24px;
    font-size: 19px;
    line-height: 1.3;
    white-space: nowrap;
  }
  .contacts li { display: flex; align-items: center; gap: 8px; }
  .contacts svg { width: 17px; height: 17px; flex: none; }

  .slogan {
    position: absolute;
    left: 0; right: 0; top: 372px;
    text-align: center;
    font-size: 20px;
    letter-spacing: 1.5px;
    color: var(--light-gray);
    text-transform: uppercase;
  }
</style>
</head>
<body>

<section class="card card--front" aria-label="Card front">
  <div class="silver-panel">
    <div class="silver-panel__frame">
      <span class="wordmark-square" aria-hidden="true"></span>
      <span class="wordmark">Belford<br>&amp; Company</span>
    </div>
  </div>
</section>

<section class="card card--back" aria-label="Card back">
  <div class="blue-panel">
    <span class="wordmark-square" aria-hidden="true"></span>
    <span class="wordmark">Belford<br>&amp; Company</span>
  </div>

  <div class="details">
    <div class="identity">
      <p class="identity__name">Daniel Hartley</p>
      <p class="identity__title">Founder</p>
      <p class="identity__address">2210 Harbor Blvd. Suite #310<br>Riverton, FL 32000</p>
    </div>
    <ul class="contacts">
      <li>
        <svg viewBox="0 0 16 16" aria-hidden="true"><path fill="currentColor" d="M3 1l3 3-1.5 2a9 9 0 0 0 5.5 5.5L12 10l3 3-2 2C6 15 1 10 1 3z"/></svg>
        555.201.4433
      </li>
      <li>
        <svg viewBox="0 0 16 16" aria-hidden="true"><rect x="4" y="1" width="8" height="14" rx="1.5" fill="none" stroke="currentColor" stroke-width="1.5"/><circle cx="8" cy="12.5" r="0.9" fill="currentColor"/></svg>
        555.201.4434
      </li>
      <li>
        <svg viewBox="0 0 16 16" aria-hidden="true"><rect x="4" y="1" width="8" height="5" fill="none" stroke="currentColor" stroke-width="1.4"/><rect x="1" y="6" width="14" height="7" rx="1" fill="currentColor"/><rect x="4" y="11" width="8" height="4" fill="currentColor"/></svg>
        555.201.4435
      </li>
      <li>
        <svg viewBox="0 0 16 16" aria-hidden="true"><rect x="1" y="3" width="14" height="10" fill="none" stroke="currentColor" stroke-width="1.4"/><path d="M1 3l7 6 7-6" fill="none" stroke="currentColor" stroke-width="1.4"/></svg>
        daniel@belfordandcompany.example
      </li>
      <li>
        <svg viewBox="0 0 16 16" aria-hidden="true"><circle cx="8" cy="8" r="6.5" fill="none" stroke="currentColor" stroke-width="1.3"/><ellipse cx="8" cy="8" rx="2.8" ry="6.5" fill="none" stroke="currentColor" stroke-width="1.1"/><path d="M1.5 8h13M2.5 5h11M2.5 11h11" stroke="currentColor" stroke-width="1"/></svg>
        www.belfordandcompany.example
      </li>
    </ul>
  </div>

  <p class="slogan">Precision Shapes Every Outcome.</p>
</section>

</body>
</html>
```